依頼詳細
購買意欲に響く電子チラシが欲しい。
記載項目
社名、情報、キャッチコピー
サイズ
A4
ページ数
片面
希望イメージ
シンプル 複雑
単色 カラフル
暗い 明るい
日常 高級
遊び心 厳粛
未来的 伝統的
女性的 男性的
希望する色
黄・オレンジ系、青系、無彩色系
納品ファイル
• 高解像度JPG (.jpg)
補足説明
販促用チラシの作成。

会員年齢層は平均40-50代が中心4000名ほど
見やすく、販促意欲を刺激するものを希望。

購入されたポイントは旅行やギフトを使えます。
会社ページ
https://www.lunafield-qz.app/

```html
<!DOCTYPE html>
<html lang="ja">
<head>
<meta charset="utf-8">
<title>Lunafield QZ RT付与率UPキャンペーン</title>
<link rel="stylesheet" href="https://fonts.googleapis.com/css2?family=Noto+Sans+JP:wght@500;700;900&family=Noto+Serif+JP:wght@500;700;900&display=swap">
<style>
:root{
  --sky-top:#3fb6e8;
  --sky-low:#bfe9f7;
  --sea:#19a3c6;
  --gold:#f4c228;
  --red:#e0211b;
  --navy:#0c1a5c;
  --navy-mid:#1b2f8a;
  --yellow:#ffe23a;
  --white:#ffffff;
  --ink:#1a1a1a;
}
*{margin:0;padding:0;box-sizing:border-box}
html,body{width:849px;height:1200px;overflow:hidden;background:var(--white)}
body{font-family:"Noto Sans JP",sans-serif;color:var(--ink)}
.flyer{position:relative;width:849px;height:1200px;overflow:hidden;background:var(--white)}
.hero-scene{position:absolute;left:0;top:0;width:849px;height:500px;
  background:linear-gradient(180deg,var(--sky-top) 0%,var(--sky-low) 45%,var(--sea) 70%,#f1d08a 100%)}
.brand{position:absolute;left:18px;top:14px;display:flex;align-items:center;gap:8px;
  font-weight:700;font-size:15px;color:var(--navy)}
.brand-dot{width:22px;height:22px;border-radius:50%;background:var(--red)}
.headline{position:absolute;left:0;width:100%;top:22px;text-align:center;
  font-weight:900;font-size:44px;color:var(--red);letter-spacing:1px;
  -webkit-text-stroke:6px var(--white);paint-order:stroke fill}
.limited{position:absolute;right:22px;top:80px;width:96px;height:128px;border-radius:14px;
  background:var(--red);color:var(--white);text-align:center;border:4px solid var(--yellow);
  font-weight:900;font-size:30px;line-height:1.1;padding-top:14px}
.limited small{display:block;font-size:14px;color:var(--yellow);margin-top:8px}
.amount{position:absolute;left:0;width:100%;top:120px;text-align:center;
  font-family:"Noto Serif JP",serif;font-weight:900;font-size:230px;line-height:1;
  color:var(--gold);-webkit-text-stroke:10px var(--ink);paint-order:stroke fill;letter-spacing:-6px}
.campaign{position:absolute;left:220px;width:410px;top:360px;height:52px;background:var(--red);
  color:var(--white);text-align:center;font-family:"Noto Serif JP",serif;font-weight:900;font-size:36px;line-height:52px}
.convert{position:absolute;left:50px;width:749px;top:412px;height:52px;background:var(--navy-mid);
  color:var(--white);text-align:center;font-weight:900;font-size:34px;line-height:52px}
.convert .arrow{color:var(--yellow)}
.bonus{position:absolute;left:0;width:100%;top:462px;text-align:center;font-weight:900;font-size:30px;
  color:var(--red);-webkit-text-stroke:5px var(--white);paint-order:stroke fill}
.gallery{position:absolute;left:0;top:500px;width:849px;height:160px;display:flex}
.gallery .shot{flex:1}
.shot-hotel{background:linear-gradient(160deg,#1c2a55,#d08a3c)}
.shot-spa{background:linear-gradient(160deg,#6b4a32,#d8c2a0)}
.shot-pool{background:linear-gradient(160deg,#f0e6d8,#46a9c9)}
.rates{position:absolute;left:0;top:668px;width:849px;height:455px;background:var(--navy);
  display:flex;flex-direction:column;gap:6px;padding:6px 0}
.rate{flex:1;display:flex;align-items:stretch}
.rate-base{width:150px;background:var(--white);padding:0 8px;font-family:"Noto Serif JP",serif;font-weight:700;
  font-size:13px;line-height:1.25;display:flex;flex-direction:column;justify-content:center;white-space:nowrap}
.rate-base b{display:block;font-size:18px}
.rate-old{width:90px;color:var(--white);font-weight:700;font-size:19px;display:flex;align-items:center;justify-content:center;white-space:nowrap}
.rate-arrow{width:30px;display:flex;align-items:center}
.rate-new{width:340px;background:var(--white);color:var(--red);font-family:"Noto Serif JP",serif;font-weight:900;
  font-size:52px;display:flex;align-items:center;justify-content:center;white-space:nowrap}
.rate-up{flex:1;color:var(--yellow);font-weight:900;display:flex;flex-direction:column;justify-content:center;padding-left:22px;font-size:18px;white-space:nowrap}
.rate-up em{font-style:normal;font-size:34px}
.rate-up span{font-size:16px;font-weight:700}
.footer{position:absolute;left:0;top:1130px;width:100%;text-align:center;line-height:1.3}
.footer-name{font-family:"Noto Sans JP",sans-serif;font-weight:700;font-size:30px;color:var(--ink)}
.footer-url{font-family:"Noto Sans JP",sans-serif;font-weight:500;font-size:17px;color:var(--ink)}
</style>
</head>
<body>
<main class="flyer">
  <div class="hero-scene" role="img" aria-label="青空と南国のビーチ、舞い上がる金色のポイントコイン"></div>
  <div class="brand"><span class="brand-dot"></span>Lunafield QZ</div>
  <p class="headline">RT付与率UPでお得！</p>
  <div class="limited">期間<br>限定<small>5/31まで</small></div>
  <h1 class="amount">1億円</h1>
  <p class="campaign">還元キャンペーン</p>
  <p class="convert">確定した報酬から<span class="arrow">➡</span>RTに変換したら</p>
  <p class="bonus">通常より断然お得！</p>
  <div class="gallery">
    <div class="shot shot-hotel" role="img" aria-label="夜景のリゾートホテル"></div>
    <div class="shot shot-spa" role="img" aria-label="スパでのリラクゼーション"></div>
    <div class="shot shot-pool" role="img" aria-label="リゾートのプールサイド"></div>
  </div>
  <section class="rates">
    <div class="rate"><div class="rate-base">通常<b>25,000円分</b></div><div class="rate-old">17.5RT</div><div class="rate-arrow"><svg width="22" height="26"><polygon points="0,0 22,13 0,26" fill="#e0211b"/></svg></div><div class="rate-new">18.5RT</div><div class="rate-up"><div>付与率 <em>5%UP</em></div><span>(1,250円お得)</span></div></div>
    <div class="rate"><div class="rate-base">通常<b>50,000円分</b></div><div class="rate-old">35RT</div><div class="rate-arrow"><svg width="22" height="26"><polygon points="0,0 22,13 0,26" fill="#e0211b"/></svg></div><div class="rate-new">38.5RT</div><div class="rate-up"><div>付与率 <em>10%UP</em></div><span>(5,000円お得)</span></div></div>
    <div class="rate"><div class="rate-base">通常<b>100,000円分</b></div><div class="rate-old">70RT</div><div class="rate-arrow"><svg width="22" height="26"><polygon points="0,0 22,13 0,26" fill="#e0211b"/></svg></div><div class="rate-new">80.5RT</div><div class="rate-up"><div>付与率 <em>15%UP</em></div><span>(15,000円お得)</span></div></div>
    <div class="rate"><div class="rate-base">通常<b>200,000円分</b></div><div class="rate-old">140RT</div><div class="rate-arrow"><svg width="22" height="26"><polygon points="0,0 22,13 0,26" fill="#e0211b"/></svg></div><div class="rate-new">168RT</div><div class="rate-up"><div>付与率 <em>20%UP</em></div><span>(40,000円お得)</span></div></div>
    <div class="rate"><div class="rate-base">通常<b>500,000円分</b></div><div class="rate-old">350RT</div><div class="rate-arrow"><svg width="22" height="26"><polygon points="0,0 22,13 0,26" fill="#e0211b"/></svg></div><div class="rate-new">437.5RT</div><div class="rate-up"><div>付与率 <em>25%UP</em></div><span>(125,000円お得)</span></div></div>
  </section>
  <footer class="footer">
    <p class="footer-name">Lunafield QZ</p>
    <p class="footer-url">https://www.lunafield-qz.app/</p>
  </footer>
</main>
</body>
</html>
```